Cardboard hanging box designs

I need to get some cardboard boxes made up for trailer wheel bearing kits. They need to be hanging boxes as pictured. The box needs to fit with our existing colour scheme and be clearly evident that it is for trailers. I am after 2 designs, one for "Trailer Bearing Kit" and one for "Marine Bearing Kit".
The Marine Bearing kit box should measure, 180mm High, 120mm Wide, 60mm Deep.
The Trailer Bearing kit box should measure, 180mm high, 120mm Wide, 30mm Deep.
These are all external measurements.

```html
<!DOCTYPE html>
<html lang="en">
<head>
<meta charset="utf-8">
<title>Korvex Parts – Wheel Bearing Kit Packaging</title>
<link rel="stylesheet" href="https://fonts.googleapis.com/css2?family=Oswald:wght@500;600;700&family=Titillium+Web:ital,wght@1,700&display=swap">
<style>
  :root {
    --page: #ffffff;
    --marine: #283283;
    --marine-light: #2f62b8;
    --trailer: #8c1218;
    --trailer-light: #c0161d;
    --yellow: #f6e03a;
    --charcoal: #2c2c2c;
    --charcoal-light: #4a4a4a;
    --steel: #8d8f94;
    --steel-light: #c9cbcf;
    --tick: #f0a818;
    --white: #ffffff;
  }
  * { box-sizing: border-box; margin: 0; padding: 0; }
  html, body { width: 1200px; height: 750px; overflow: hidden; background: var(--page); }
  .canvas { position: relative; width: 1200px; height: 750px; }

  .pack {
    position: absolute; top: 50px; width: 290px;
    --main: var(--marine); --main-light: var(--marine-light);
  }
  .pack--marine { left: 215px; }
  .pack--trailer { left: 695px; --main: var(--trailer); --main-light: var(--trailer-light); }

  .hang-tab { height: 120px; background: var(--main); position: relative; }
  .hang-slot { position: absolute; left: 50%; top: 42px; transform: translateX(-50%); }

  .front { height: 520px; display: flex; flex-direction: column; overflow: hidden; }

  .top-band {
    height: 56px; background: var(--main);
    display: flex; flex-direction: column; align-items: center; justify-content: center;
    color: var(--white); font-family: "Oswald", sans-serif; line-height: 1;
  }
  .top-band .kit-name { font-size: 19px; font-weight: 600; }
  .top-band .kit-type { font-size: 8px; font-weight: 500; margin-top: 3px; letter-spacing: .3px; }

  .stripe { height: 10px; background: var(--yellow); flex: none; }

  .brand-panel {
    height: 150px;
    background: radial-gradient(ellipse at 50% 45%, var(--charcoal-light), var(--charcoal) 75%);
    display: flex; align-items: center; justify-content: center;
  }
  .brand-name {
    font-family: "Oswald", sans-serif; font-weight: 700; font-size: 42px;
    color: var(--yellow); letter-spacing: 1px; line-height: 1; text-align: center;
  }

  .product-panel {
    flex: 1; position: relative; padding: 16px 18px 0;
    background: linear-gradient(160deg, var(--main-light) 0%, var(--main) 70%);
  }
  .title {
    font-family: "Oswald", sans-serif; color: var(--white); line-height: 1; text-align: right;
    padding-right: 8px;
  }
  .title .main { font-size: 31px; font-weight: 600; display: block; }
  .title .sub { font-size: 17px; font-weight: 600; display: block; margin-top: 3px; padding-right: 60px; }

  .bearing-image {
    position: absolute; left: 10px; top: 86px; width: 96px; height: 82px;
    border-radius: 40% 40% 30% 30%;
    background: radial-gradient(ellipse at 45% 40%, var(--steel-light), var(--steel) 70%);
  }
  .claim {
    position: absolute; left: 92px; top: 108px; width: 122px; height: 30px;
    background: var(--yellow); color: var(--charcoal);
    font-family: "Oswald", sans-serif; font-weight: 600; font-size: 15px;
    display: flex; align-items: center; justify-content: center; letter-spacing: .5px;
  }
  .checker { position: absolute; right: 14px; top: 80px; }

  .features {
    position: absolute; left: 14px; right: 12px; top: 186px; list-style: none;
    font-family: "Titillium Web", sans-serif; font-style: italic; font-weight: 700;
    font-size: 8.6px; color: var(--white); line-height: 1.35; letter-spacing: .3px;
  }
  .features li { display: flex; align-items: flex-start; gap: 8px; margin-bottom: 6px; }
  .features svg { flex: none; margin-top: 1px; }
</style>
</head>
<body>
<div class="canvas">

  <section class="pack pack--marine" aria-label="Marina wheel bearing kit box">
    <div class="hang-tab">
      <svg class="hang-slot" width="48" height="26" viewBox="0 0 48 26" aria-hidden="true">
        <path d="M8 10 H18 A6 6 0 0 1 30 10 H40 A6 6 0 0 1 40 24 H8 A6 6 0 0 1 8 10 Z" fill="#fff"/>
      </svg>
    </div>
    <div class="front">
      <header class="top-band">
        <span class="kit-name">MARINA KIT</span>
        <span class="kit-type">WHEEL BEARING KIT</span>
      </header>
      <div class="stripe"></div>
      <div class="brand-panel"><span class="brand-name">KORVEX<br>PARTS</span></div>
      <div class="stripe"></div>
      <div class="product-panel">
        <h2 class="title"><span class="main">WHEEL BEARING KIT</span><span class="sub">MARINA KIT</span></h2>
        <div class="bearing-image" role="img" aria-label="Photo of a tapered roller bearing and race"></div>
        <div class="claim">&amp; DURABLE</div>
        <svg class="checker" width="46" height="90" viewBox="0 0 46 90" aria-hidden="true">
          <rect x="23" y="0" width="23" height="40" fill="var(--yellow)"/>
          <rect x="0" y="40" width="23" height="30" fill="var(--yellow)"/>
          <rect x="23" y="70" width="18" height="20" fill="var(--yellow)"/>
        </svg>
        <ul class="features">
          <li><svg width="12" height="14" viewBox="0 0 12 14"><path d="M1 8 L4 12 L11 1" fill="none" stroke="var(--tick)" stroke-width="2.2"/></svg>HEAVY DUTY BEARINGS FOR EXTENDED SEVICE LIFE</li>
          <li><svg width="12" height="14" viewBox="0 0 12 14"><path d="M1 8 L4 12 L11 1" fill="none" stroke="var(--tick)" stroke-width="2.2"/></svg>PRECISION ENGINEERED BEARING RACES PROVIDE MAXIMUM LOAD CAPACITY</li>
          <li><svg width="12" height="14" viewBox="0 0 12 14"><path d="M1 8 L4 12 L11 1" fill="none" stroke="var(--tick)" stroke-width="2.2"/></svg>HIGH QUALITY OIL SEALS ELIMINATE BEARING CONTAMINATION</li>
        </ul>
      </div>
    </div>
  </section>

  <section class="pack pack--trailer" aria-label="Trailer wheel bearing kit box">
    <div class="hang-tab">
      <svg class="hang-slot" width="48" height="26" viewBox="0 0 48 26" aria-hidden="true">
        <path d="M8 10 H18 A6 6 0 0 1 30 10 H40 A6 6 0 0 1 40 24 H8 A6 6 0 0 1 8 10 Z" fill="#fff"/>
      </svg>
    </div>
    <div class="front">
      <header class="top-band">
        <span class="kit-name">TRAILER KIT</span>
        <span class="kit-type">WHEEL BEARING KIT</span>
      </header>
      <div class="stripe"></div>
      <div class="brand-panel"><span class="brand-name">KORVEX<br>PARTS</span></div>
      <div class="stripe"></div>
      <div class="product-panel">
        <h2 class="title"><span class="main">WHEEL BEARING KIT</span><span class="sub">TRAILER KIT</span></h2>
        <div class="bearing-image" role="img" aria-label="Photo of a tapered roller bearing and race"></div>
        <div class="claim">&amp; DURABLE</div>
        <svg class="checker" width="46" height="90" viewBox="0 0 46 90" aria-hidden="true">
          <rect x="23" y="0" width="23" height="40" fill="var(--yellow)"/>
          <rect x="0" y="40" width="23" height="30" fill="var(--yellow)"/>
          <rect x="23" y="70" width="18" height="20" fill="var(--yellow)"/>
        </svg>
        <ul class="features">
          <li><svg width="12" height="14" viewBox="0 0 12 14"><path d="M1 8 L4 12 L11 1" fill="none" stroke="var(--tick)" stroke-width="2.2"/></svg>HEAVY DUTY BEARINGS FOR EXTENDED SEVICE LIFE</li>
          <li><svg width="12" height="14" viewBox="0 0 12 14"><path d="M1 8 L4 12 L11 1" fill="none" stroke="var(--tick)" stroke-width="2.2"/></svg>PRECISION ENGINEERED BEARING RACES PROVIDE MAXIMUM LOAD CAPACITY</li>
          <li><svg width="12" height="14" viewBox="0 0 12 14"><path d="M1 8 L4 12 L11 1" fill="none" stroke="var(--tick)" stroke-width="2.2"/></svg>HIGH QUALITY OIL SEALS ELIMINATE BEARING CONTAMINATION</li>
        </ul>
      </div>
    </div>
  </section>

</div>
</body>
</html>
```